Modern business card and stationary design for Tech consulting company (startup)
Veromb Technologies Limited
Modern business card and stationary design for Tech consulting company (startup) - Information Technology
Creative Brief
Professional
Malcolm Dewhurst
CEO
Suite 24613 Lower Ground Floor 212-224 Harwell Road London, N7 2QD
mdewhurst@veromb.co.uk
www.veromb.co.uk
Designers, This project is for business card and stationary design. What I’m looking for is design based around the colour scheme of the attached logo. As yet the website is still being designed, but the attached business logo will give you a reference point for the corporate colours. I have attached a couple of links with a general idea of what I’m looking for; http://www.plandoria.com/drafts/display/contest/518230/draft/3047612 http://www.plandoria.com/drafts/display/contest/518230/draft/3048945 All submitted designs will be rated on a regular basis. If you have any further questions relating to this project, please let get in touch. The winning design will be required to provide editable versions of the files (i.e. personal contact details etc.) Good luck

```html
<!DOCTYPE html>
<html lang="en">
<head>
<meta charset="utf-8">
<title>Veromb Technologies – Business Card</title>
<link rel="stylesheet" href="https://fonts.googleapis.com/css2?family=Open+Sans:wght@400;600;700&display=swap">
<style>
  :root {
    --backdrop: #e9e6e2;
    --card-white: #ffffff;
    --brand-red: #d9252b;
    --brand-red-deep: #b51a20;
    --swoosh-grey: #b9bcc0;
    --swoosh-light: #dfe1e3;
    --ink-dark: #3a3d42;
    --text-light: #ffffff;
    --divider: rgba(255,255,255,0.7);
  }
  * { margin: 0; padding: 0; box-sizing: border-box; }
  html, body {
    width: 1200px; height: 914px; overflow: hidden;
    background: var(--backdrop);
    font-family: "Open Sans", Arial, sans-serif;
  }
  .business-card {
    position: absolute; left: 75px; top: 157px;
    width: 1050px; height: 600px;
    background: var(--card-white);
    overflow: hidden;
    box-shadow: 0 10px 30px rgba(0,0,0,0.18);
  }
  .card-waves { position: absolute; inset: 0; width: 100%; height: 100%; }
  .brand-mark {
    position: absolute; left: 360px; top: 140px;
    display: flex; align-items: center; gap: 18px;
  }
  .brand-square { width: 54px; height: 54px; background: var(--ink-dark); }
  .brand-name {
    font-size: 44px; font-weight: 700; letter-spacing: 2px;
    color: var(--ink-dark); text-transform: uppercase; line-height: 1;
  }
  .holder-block {
    position: absolute; left: 150px; top: 385px; width: 350px;
    text-align: right; color: var(--text-light);
  }
  .holder-name { font-size: 24px; font-weight: 700; line-height: 1.2; }
  .holder-role { font-size: 19px; font-weight: 600; margin-bottom: 6px; }
  .holder-address { font-size: 18px; line-height: 1.4; font-weight: 400; }
  .contact-divider {
    position: absolute; left: 530px; top: 395px; width: 2px; height: 160px;
    background: var(--divider);
  }
  .contact-list {
    position: absolute; left: 555px; top: 392px; list-style: none;
    color: var(--text-light); font-size: 18px;
  }
  .contact-item { display: flex; align-items: center; gap: 14px; height: 41px; }
  .contact-icon { width: 26px; height: 26px; flex: none; }
</style>
</head>
<body>
  <div class="business-card">
    <svg class="card-waves" viewBox="0 0 1050 600" preserveAspectRatio="none" aria-hidden="true">
      <path d="M0 300 C 250 250, 600 330, 1050 250 L1050 330 C 650 390, 300 300, 0 345 Z" fill="var(--swoosh-light)"/>
      <path d="M0 315 C 260 280, 620 350, 1050 285 L1050 335 C 650 385, 300 315, 0 350 Z" fill="var(--swoosh-grey)"/>
      <path d="M0 350 C 300 318, 650 392, 1050 335 L1050 600 L0 600 Z" fill="var(--brand-red)"/>
      <path d="M0 350 C 300 318, 650 392, 1050 335 L1050 345 C 650 402, 300 328, 0 360 Z" fill="var(--brand-red-deep)"/>
    </svg>

    <div class="brand-mark">
      <span class="brand-square"></span>
      <span class="brand-name">Veromb Technologies</span>
    </div>

    <div class="holder-block">
      <p class="holder-name">Malcolm Dewhurst</p>
      <p class="holder-role">CEO</p>
      <p class="holder-address">Suite 24613 Lower Ground Floor<br>212-224 Harwell Road<br>London, N7 2QD</p>
    </div>

    <div class="contact-divider"></div>

    <ul class="contact-list">
      <li class="contact-item">
        <svg class="contact-icon" viewBox="0 0 26 26" aria-hidden="true"><circle cx="13" cy="13" r="13" fill="#fff"/><path d="M9 7 l3 3 -1.5 2 a8 8 0 0 0 4.5 4.5 l2-1.5 3 3 -2 2 C12 19 7 14 7 9 Z" fill="var(--brand-red)"/></svg>
        <span>+44 (0)845 3917206</span>
      </li>
      <li class="contact-item">
        <svg class="contact-icon" viewBox="0 0 26 26" aria-hidden="true"><circle cx="13" cy="13" r="13" fill="#fff"/><rect x="9" y="6" width="8" height="14" rx="1.5" fill="var(--brand-red)"/><rect x="10.5" y="8" width="5" height="9" fill="#fff"/></svg>
        <span>+44 (0)7823 514069</span>
      </li>
      <li class="contact-item">
        <svg class="contact-icon" viewBox="0 0 26 26" aria-hidden="true"><circle cx="13" cy="13" r="13" fill="#fff"/><rect x="6" y="8" width="14" height="10" fill="var(--brand-red)"/><path d="M6 8 l7 6 7-6" fill="none" stroke="#fff" stroke-width="1.3"/></svg>
        <span>mdewhurst@veromb.co.uk</span>
      </li>
      <li class="contact-item">
        <svg class="contact-icon" viewBox="0 0 26 26" aria-hidden="true"><circle cx="13" cy="13" r="13" fill="#fff"/><circle cx="13" cy="13" r="7" fill="none" stroke="var(--brand-red)" stroke-width="1.6"/><ellipse cx="13" cy="13" rx="3" ry="7" fill="none" stroke="var(--brand-red)" stroke-width="1.3"/><line x1="6" y1="13" x2="20" y2="13" stroke="var(--brand-red)" stroke-width="1.3"/></svg>
        <span>www.veromb.co.uk</span>
      </li>
    </ul>
  </div>
</body>
</html>
```